New Business Card Design Project

I would like a business card to match my truck wrap and logo. I would like the font to match my existing business card please.

Industry/Entity Type

Painter

Contact Information for Business Card

Rodrigo Venter 801-437-2910 Ventercoatings.utah@brushmail.net
SERVICES - Custom Paint & Stain, Interior & Exterior, Epoxy Coatings / Garage Floors, Cabinet Refinishing, Log Staining and Refinishing.

Requirements
Nice to have
• I would like to have the white and grey line like the bottom of my vehicle wrap, Light Grey to match my truck also.

```html
<!DOCTYPE html>
<html lang="en">
<head>
<meta charset="utf-8">
<title>Venter Coatings – Business Card</title>
<link href="https://fonts.googleapis.com/css2?family=Saira:wght@500;600;700&display=swap" rel="stylesheet">
<style>
  :root {
    --brand-blue: #05adee;
    --wrap-grey: #9ca1ac;
    --ink-dark: #333538;
    --paper: #ffffff;
    --canvas: #ffffff;
  }
  html, body {
    margin: 0;
    padding: 0;
    width: 1200px;
    height: 1200px;
    overflow: hidden;
    background: var(--canvas);
  }
  .sheet {
    position: relative;
    width: 1200px;
    height: 1200px;
    font-family: "Saira", "Arial Narrow", sans-serif;
  }
  .card {
    position: absolute;
    left: 233px;
    width: 734px;
    height: 407px;
    background: var(--paper);
    box-shadow: 0 6px 40px rgba(0, 0, 0, 0.08);
    overflow: hidden;
  }
  .card--front { top: 163px; }
  .card--back { top: 630px; }
  .card svg { display: block; width: 734px; height: 407px; }
  .brand-name {
    font-family: "Saira", "Arial Narrow", sans-serif;
    font-weight: 700;
    fill: var(--brand-blue);
    letter-spacing: 2px;
  }
  .brand-mark { fill: var(--brand-blue); }
  .person-name { font-weight: 600; fill: var(--brand-blue); font-size: 36px; letter-spacing: 2px; }
  .person-role { font-weight: 600; fill: var(--brand-blue); font-size: 18px; letter-spacing: 2px; }
  .contact-text { font-weight: 500; fill: var(--ink-dark); font-size: 25px; letter-spacing: 2px; }
  .contact-email { font-size: 21px; letter-spacing: 1px; }
  .services-title { font-weight: 600; fill: #fff; font-size: 32px; letter-spacing: 2px; }
  .service-item { font-weight: 600; fill: #fff; font-size: 23px; letter-spacing: 1.5px; }
  .band-blue { fill: var(--brand-blue); }
  .band-grey { fill: none; stroke: var(--wrap-grey); stroke-width: 12; }
  .band-white { fill: none; stroke: #fff; stroke-width: 10; }
  .rule { stroke: var(--brand-blue); stroke-width: 1.5; }
  .icon-disc { fill: var(--ink-dark); }
  .icon-line { fill: none; stroke: #fff; stroke-width: 2.5; stroke-linejoin: round; stroke-linecap: round; }
</style>
</head>
<body>
<main class="sheet">

  <section class="card card--front" aria-label="Card front">
    <svg viewBox="0 0 1182 656" xmlns="http://www.w3.org/2000/svg">
      <rect class="brand-mark" x="120" y="268" width="110" height="110" rx="10"/>
      <text class="brand-name" x="262" y="358" font-size="76">VENTER COATINGS</text>
    </svg>
  </section>

  <section class="card card--back" aria-label="Card back">
    <svg viewBox="0 0 1182 656" xmlns="http://www.w3.org/2000/svg">
      <!-- top wrap stripe -->
      <polygon class="band-blue" points="635,0 1182,0 1182,66 675,66"/>
      <polyline class="band-white" points="663,-5 693,42 1190,42"/>

      <!-- bottom wrap band -->
      <polygon class="band-blue" points="0,604 513,604 687,316 1182,316 1182,656 0,656"/>
      <polyline class="band-grey" points="-5,584 502,584 678,298 1190,298"/>

      <!-- brand -->
      <rect class="brand-mark" x="58" y="120" width="82" height="82" rx="8"/>
      <text class="brand-name" x="160" y="180" font-size="44">VENTER COATINGS</text>

      <!-- person -->
      <text class="person-name" x="40" y="351">RODRIGO VENTER</text>
      <text class="person-role" x="41" y="379">MANAGER</text>
      <line class="rule" x1="42" y1="392" x2="582" y2="392"/>

      <!-- phone -->
      <circle class="icon-disc" cx="58" cy="444" r="22"/>
      <path class="icon-line" d="M50 433 l5 -2 l4 7 l-3 3 q3 6 8 9 l3 -3 l7 4 l-2 5 q-14 1 -22 -23 z"/>
      <text class="contact-text" x="96" y="453">801-437-2910</text>

      <!-- email -->
      <circle class="icon-disc" cx="58" cy="506" r="22"/>
      <rect class="icon-line" x="45" y="497" width="26" height="18" rx="1"/>
      <polyline class="icon-line" points="45,497 58,508 71,497"/>
      <polyline class="icon-line" points="45,515 54,505"/>
      <polyline class="icon-line" points="71,515 62,505"/>
      <text class="contact-text contact-email" x="96" y="514">ventercoatings.utah@brushmail.net</text>

      <!-- services -->
      <text class="services-title" x="1146" y="382" text-anchor="end">SERVICES</text>
      <g class="service-list">
        <text class="service-item" x="1100" y="430" text-anchor="end">CUSTOM PAINT &amp; STAIN</text>
        <circle cx="1135" cy="422" r="9" fill="#fff"/>
        <text class="service-item" x="1100" y="474" text-anchor="end">INTERIOR &amp; EXTERIOR</text>
        <circle cx="1135" cy="466" r="9" fill="#fff"/>
        <text class="service-item" x="1100" y="517" text-anchor="end">EPOXY COATINGS / GARAGE FLOORS</text>
        <circle cx="1135" cy="509" r="9" fill="#fff"/>
        <text class="service-item" x="1100" y="561" text-anchor="end">CABINET REFINISHING</text>
        <circle cx="1135" cy="553" r="9" fill="#fff"/>
        <text class="service-item" x="1100" y="605" text-anchor="end">LOG STAINING &amp; REFINISHING</text>
        <circle cx="1135" cy="597" r="9" fill="#fff"/>
      </g>
    </svg>
  </section>

</main>
</body>
</html>
```